Lantern Ministries needs a book cover (front, spine & back). Title of book is "Eternity: ...

Book title: Eternity: Which Road Shall We Walk?

Book size: 5.5 X 8.5 X ½” spine (include standard bleed)

File: Would like to receive as an Adobe Photoshop file with layers

Components of the front cover:

1. The Gate representing “Heaven’s Gate.” Use the gate I uploaded to your site unless you can find a more attractive ornate gate better than this one that fits this imagery. I’m searching for a look that draws a “Wow!” out of the person looking at it as well as for the entire cover.

a. Instructions for gate: I do not want it black. Please make the color gold or as close to the color gold as you can. And not just the same one color but variations. You can try white or mother of pearl if you think it looks better as contrasted with your background. But not red, orange, yellow, green, blue, or purple.

2. An angel who stands in front of the right side of the gate from the reader’s viewpoint. It must be within these parameters:

a. Height: Standing on the ground in front of the gate, His head should be in line with the top of the circle in the ornate “T” figure on the top of the right white column.

b. Width: Stay within the width of the right gate but don’t cover the filigree in the middle of the gate.

c. He is holding a sword pointing to the ground whose blade looks like a laser beam.

d. He should have medium size wings about 2/3 his height not the length of his body.

e. No halo please

f. He should look like what is conveyed in this Bible scripture:

Matthew 28:2-4 NIV – There was a violent earthquake, for an angel of the Lord came down from heaven and, going to the tomb, rolled back the stone and sat on it. 3. His appearance was like lightning, and his clothes were white as snow. 4. The guards were so afraid of him that they shook and became like dead men.

“His appearance” In our language the word "countenance" refers to the "face only;" in the original it refers to his "whole person." His "general aspect, or the appearance of the angel himself," was, etc.

“Like lightning” Peculiarly bright and shining.

“His clothes were white as snow” Celestial beings are usually represented as clothed in white, Acts 1:10; Dan 7:9; Rev 3:4-5; 4:4; 7:13-14.

3. The background behind the gate needs to capture the grandeur and purity of Heaven. I’d like to see light colors instead of dark. Even a 3D effect might be interesting in contrast with the gate if you think it works.

4. Text: (use a font that matches the feel of the word Heaven)

a. Title of book: Eternity: Which Road Shall We Walk (note subtitle may change slightly).

b. Author’s name: “Marcus Throlden” (Note: my name does not have to be on the front cover if it’s going to take away from the overall feel, or if fitting it on the page is a problem. By no means make the other components have to accommodate it).

Components of the spine:

1. Carryover visual matching the front cover.

2. Text:

b. Author’s name: “Marcus Throlden”

c. Space for Vendoro’s publishing logo

Components of the back cover:

1. Carryover complementing the front cover.

2. I do not have the copy yet for the back cover.

Requirements
Must have
• Use light colors for heaven's background, especially shades of white and golden hues, not dark colors. Also avoid using clouds.
• An additional note on specs about the angel:
• 1. His wings should not be extended in a flying motion but rather in a closed position at his back no more than 2/3's of his size.
• 2. He should have white robes, and together with his face, be barely seen while white light glows and emanates from him. See uploaded picture of angel for a rough idea of what I'm looking for.

```html
<!DOCTYPE html>
<html lang="en">
<head>
<meta charset="utf-8">
<title>Eternity: Which Road Shall We Walk — Book Cover Spread</title>
<link href="https://fonts.googleapis.com/css2?family=Cinzel:wght@400;500&family=Arimo&display=swap" rel="stylesheet">
<style>
  :root {
    --stage: #a3a3a3;
    --trim: #ffffff;
    --back-blue: #3a9bda;
    --sky-deep: #2f8fe0;
    --sky-mid: #6fb9f0;
    --sky-light: #d9eefc;
    --glow: #ffffff;
    --ink-dark: #15181c;
    --ink-light: #ffffff;
    --photo-box: #fdeded;
    --logo-box: #ffffff;
    --spine-line: rgba(120, 140, 160, 0.6);
  }
  * { margin: 0; padding: 0; box-sizing: border-box; }
  html, body { width: 1200px; height: 800px; overflow: hidden; background: var(--stage); }

  .spread {
    position: absolute; left: 57px; top: 24px;
    width: 1085px; height: 752px;
    background: var(--trim);
  }
  .back-cover {
    position: absolute; left: 9px; top: 9px;
    width: 490px; height: 733px;
    background: var(--back-blue);
    overflow: hidden;
  }
  .spine {
    position: absolute; left: 499px; top: 9px;
    width: 88px; height: 733px;
    border-left: 1px solid var(--spine-line);
    border-right: 1px solid var(--spine-line);
    overflow: hidden;
  }
  .front-cover {
    position: absolute; left: 587px; top: 9px;
    width: 489px; height: 733px;
    overflow: hidden;
  }

  .sky-art {
    position: absolute; inset: 0;
    background:
      radial-gradient(ellipse 60% 40% at 50% 48%, rgba(255,255,255,0.85), rgba(255,255,255,0) 70%),
      radial-gradient(ellipse 40% 60% at 100% 30%, rgba(255,255,255,0.9), rgba(255,255,255,0) 70%),
      radial-gradient(ellipse 45% 50% at 0% 45%, rgba(255,255,255,0.85), rgba(255,255,255,0) 70%),
      radial-gradient(ellipse 70% 30% at 50% 0%, rgba(255,255,255,0.85), rgba(255,255,255,0) 70%),
      linear-gradient(180deg, var(--sky-deep) 0%, var(--sky-mid) 45%, var(--sky-light) 80%, var(--glow) 100%);
  }
  .spine .sky-art {
    background:
      radial-gradient(ellipse 80% 20% at 50% 10%, rgba(255,255,255,0.85), rgba(255,255,255,0) 70%),
      radial-gradient(ellipse 90% 25% at 50% 50%, rgba(255,255,255,0.75), rgba(255,255,255,0) 70%),
      linear-gradient(180deg, var(--sky-mid) 0%, var(--sky-light) 60%, var(--glow) 100%);
  }
  .gate-art {
    position: absolute; left: 60px; top: 267px;
    width: 300px; height: 420px;
    border-radius: 46% 46% 10% 10% / 30% 30% 6% 6%;
    background:
      linear-gradient(180deg, rgba(70,100,130,0.55) 0%, rgba(120,170,215,0.55) 55%, rgba(220,238,252,0.4) 85%, rgba(255,255,255,0) 100%);
    filter: blur(2px);
  }

  .title {
    font-family: "Cinzel", serif;
    font-weight: 400;
    text-align: center;
  }
  .back-cover .title {
    position: absolute; left: 0; width: 100%; top: 48px;
    font-size: 40px; letter-spacing: 10px; color: var(--ink-light);
    text-shadow: 1px 1px 2px rgba(0,0,0,0.35);
  }
  .back-cover .subtitle {
    position: absolute; left: 0; width: 100%; top: 104px;
    font-family: "Cinzel", serif; font-size: 16px; letter-spacing: 2px;
    text-align: center; color: var(--ink-light);
    text-shadow: 1px 1px 2px rgba(0,0,0,0.35);
  }
  .blurb {
    position: absolute; font-family: "Arimo", sans-serif;
    color: var(--ink-light); text-align: justify;
  }
  .blurb-lead { left: 15px; top: 180px; width: 449px; font-size: 15px; line-height: 19.5px; letter-spacing: -0.6px; }
  .blurb-bio { left: 148px; top: 380px; width: 316px; font-size: 13.4px; line-height: 18.2px; letter-spacing: -0.6px; }
  .author-photo {
    position: absolute; left: 23px; top: 382px; width: 113px; height: 156px;
    background: var(--photo-box);
  }
  .logo-slot {
    position: absolute; left: 15px; top: 639px; width: 157px; height: 73px;
    background: var(--logo-box);
  }

  .spine-text {
    position: absolute; left: 50%;
    writing-mode: vertical-rl;
    transform: translateX(-50%);
    font-family: "Cinzel", serif; color: var(--ink-dark);
    text-shadow: 1px 1px 1px rgba(255,255,255,0.6);
    white-space: nowrap;
  }
  .spine-title { top: 59px; font-size: 46px; letter-spacing: 1px; }
  .spine-author { top: 427px; font-size: 20px; letter-spacing: 2px; }

  .front-cover .title {
    position: absolute; left: 0; width: 100%; top: 40px;
    font-size: 62px; letter-spacing: 10px; color: var(--ink-light);
    text-shadow: 2px 2px 3px rgba(0,0,0,0.55);
  }
  .front-cover .subtitle {
    position: absolute; left: 0; width: 100%; top: 118px;
    font-family: "Cinzel", serif; font-size: 19px; letter-spacing: 2.5px;
    text-align: center; color: var(--ink-light);
    text-shadow: 1px 1px 2px rgba(0,0,0,0.6);
  }
  .front-author {
    position: absolute; left: 0; width: 100%; top: 670px;
    font-family: "Cinzel", serif; font-size: 28px; letter-spacing: 8px;
    text-align: center; color: var(--ink-dark);
  }
</style>
</head>
<body>
  <div class="spread">
    <section class="back-cover">
      <h2 class="title">ETERNITY</h2>
      <p class="subtitle">WHICH ROAD SHALL WE WALK</p>
      <p class="blurb blurb-lead">Lorem ipsum dolor sit amet, consectetur adipiscing elit, sed do eiusmod tempor incididunt ut labore et dolore magna aliqua. Ut enim ad minim veniam, quis nostrud exercitation ullamco laboris nisi ut aliquip ex ea commodo consequat. Lorem ipsum dolor sit amet, consectetur adipiscing elit, sed do eiusmod tempor incididunt ut labore et dolore magna aliqua. Ut enim ad minim veniam, quis nostrud exercitation ullamco laboris nisi ut aliquip ex ea commodo consequat.</p>
      <div class="author-photo" role="img" aria-label="Author photo placeholder"></div>
      <p class="blurb blurb-bio">Lorem ipsum dolor sit amet, consectetur adipiscing elit, sed do eiusmod tempor incididunt ut labore et dolore magna aliqua. Ut enim ad minim veniam, quis nostrud exercitation ullamco laboris nisi ut aliquip ex ea commodo consequat. Lorem ipsum dolor sit amet, consectetur adipiscing elit, sed do eiusmod tempor incididunt ut labore et dolore magna aliqua. Ut enim ad minim veniam, quis nostrud exercitation ullamco laboris nisi ut aliquip ex ea commodo consequat.</p>
      <div class="logo-slot"></div>
    </section>

    <section class="spine">
      <div class="sky-art" role="img" aria-label="Bright sky with soft white clouds"></div>
      <span class="spine-text spine-title">ETERNITY</span>
      <span class="spine-text spine-author">MARCUS THROLDEN</span>
    </section>

    <section class="front-cover">
      <div class="sky-art" role="img" aria-label="Heavenly sky framed by clouds with light rays radiating from the centre"></div>
      <div class="gate-art" role="img" aria-label="Ornate wrought-iron gate between stone pillars atop misty steps"></div>
      <h1 class="title">ETERNITY</h1>
      <p class="subtitle">WHICH ROAD SHALL WE WALK</p>
      <p class="front-author">MARCUS THROLDEN</p>
    </section>
  </div>
</body>
</html>
```